Project Management - Web Design Project

Vantrel 4 Management Limited is a company which provides specialist Project Control and Contract Management expertise to the Engineering, Construction and Manufacturing industries. The emphasis is on advanced Project Management techniques in particular Planning & Scheduling, Cost Control, Change Control, Risk Management, Reporting and Contract Administration. We are a global company (albeit a small start-up at this time) and pride ourselves on our ability to support projects to help them achieve their goals and objectives. Our aim is to implement work class control tools in a simple and user friendly manner. We would like the website to appear professional but at the same time easy to navigate and a good balance between text and pictures. The final design should communicate our value added service to our customers, our willingness to support and our structured approach to our work.

Target Market(s)

Project Management professionals working for engineering, construction and manufacturing organisations involved with delivering projects.

Industry/Entity Type

Construction

Requirements
Must have
• The website must include all of the content from the attached Excel brief. The company logo (attached) must also be included in the design. The design must portray a professional look and feel. Please include pictures and photographs related to project management in the engineering, construction and manufacturing industries. We may supplement with pictures of our own during the next steps.
Nice to have
• Emphasis that Vantrel 4 is available to support, guide, direct to achieve positive outcomes for the projects. We work hard at developing our customer relationships. Our employees are experienced in advanced project management techniques.
Should not have
• The design should not use old style fonts. It should look modern and professional. Do not include cartoons or silly illustrations.

```html
<!DOCTYPE html>
<html lang="en">
<head>
<meta charset="utf-8">
<title>Vantrel 4 Management Limited</title>
<link href="https://fonts.googleapis.com/css2?family=Ubuntu:wght@300;400;500;700&family=Arimo:wght@400&display=swap" rel="stylesheet">
<style>
:root{
  --cream:#f7f3e8;
  --cream-deep:#efe8d6;
  --topline:#4a4640;
  --ink:#3b3b3b;
  --nav:#3d3d3d;
  --nav-active:#2a7bd0;
  --blue:#1e6ec4;
  --brand:#56606b;
  --hero-blue:#5c83bd;
  --text-grey:#7c7c7c;
  --rule:#d9d6cc;
  --footer:#050505;
  --footer-text:#c9c9c9;
  --footer-link:#4aa3e6;
  --white:#ffffff;
}
*{margin:0;padding:0;box-sizing:border-box}
html,body{width:1200px;height:1190px;overflow:hidden;background:var(--cream)}
body{font-family:"Ubuntu",sans-serif;color:var(--ink);position:relative}
.page{position:relative;width:1200px;height:1190px;overflow:hidden}

/* header */
.site-header{position:absolute;left:0;top:0;width:1200px;height:168px;
  background:linear-gradient(180deg,#f9f6ee 0%,var(--cream) 60%,var(--cream-deep) 100%);
  border-top:4px solid var(--topline);border-bottom:1px solid #d6d1c3}
.brand{position:absolute;left:118px;top:108px;display:flex;align-items:center;gap:8px}
.brand-square{width:14px;height:14px;background:var(--brand)}
.brand-name{font-weight:500;font-size:17px;color:var(--brand);white-space:nowrap}
.social-buttons{position:absolute;top:26px;left:933px;display:flex;gap:6px;font-family:"Arimo",sans-serif;font-size:11px}
.btn-like,.btn-count,.btn-follow{height:19px;line-height:17px;border:1px solid #c8c8c8;border-radius:3px;background:#f4f4f4;color:#3b5998;padding:0 5px}
.btn-count{color:#555;background:#fff}
.btn-follow{margin-left:8px;color:#333;font-weight:bold;padding:0 6px}
.main-nav{position:absolute;top:109px;left:407px;display:flex;font-size:14.5px;font-weight:300}
.main-nav a{color:var(--nav);text-decoration:none;padding:2px 14px 0;border-left:1px solid #d2ccbc;line-height:20px;height:26px}
.main-nav a:first-child{border-left:none;color:var(--nav-active)}

/* hero */
.hero{position:absolute;left:0;top:168px;width:1200px;height:452px;background:var(--hero-blue);overflow:hidden}
.hero-photo{position:absolute;left:520px;top:0;width:680px;height:452px;
  background:linear-gradient(90deg,var(--hero-blue) 0%,#8eaed6 18%,#c9d8e8 40%,#c99b3a 62%,#b07c2a 80%,#7a6a55 100%)}
.hero-title{position:absolute;left:124px;top:113px;color:var(--white);font-weight:500;font-size:36px;letter-spacing:-1.4px;white-space:nowrap}
.hero-copy{position:absolute;left:124px;top:167px;width:400px;color:var(--white);font-weight:300;font-size:13.8px;line-height:16.9px;letter-spacing:-.2px}
.cta{position:absolute;left:121px;top:315px;width:335px;height:58px;border-radius:6px;display:flex}
.cta-signup{width:167px;height:58px;background:#fff;border-radius:6px 0 0 6px;position:relative}
.cta-signup svg{position:absolute;left:9px;top:20px}
.cta-signup .big{position:absolute;left:52px;top:14px;font-weight:700;font-size:17px;color:#111;letter-spacing:-.3px}
.cta-signup .small{position:absolute;left:52px;top:32px;font-weight:500;font-size:11px;color:#111;letter-spacing:-.3px}
.cta-contact{width:168px;height:58px;background:linear-gradient(180deg,#3a3a3a,#101010);border-radius:0 6px 6px 0;color:#fff;text-align:center;padding-top:7px}
.cta-contact .label{font-size:16px;font-weight:400}
.cta-contact .phone{font-size:16.5px;font-weight:500;margin-top:2px}
.cta-or{position:absolute;left:149px;top:-12px;width:32px;height:32px;border-radius:50%;background:#fff;color:#333;font-size:13px;text-align:center;line-height:28px}

/* content */
.content{position:absolute;left:0;top:620px;width:1200px;height:502px;
  background:linear-gradient(180deg,#f6f1e2 0%,#f3f3ee 30%,#e7eff7 55%,#f4f1e6 100%);border-top:2px solid #e5e0d2}
.section-title{font-weight:400;font-size:23px;color:var(--blue);letter-spacing:-.4px}
.prime{position:absolute;left:112px;top:27px;width:628px}
.prime p{margin-top:12px;font-weight:300;font-size:13.6px;line-height:18px;color:var(--text-grey);letter-spacing:-.15px}
.divider{position:absolute;left:764px;top:30px;width:1px;height:440px;background:var(--rule)}
.deliverables{position:absolute;left:802px;top:27px;width:300px}
.deliverables ul{list-style:none;margin-top:10px;margin-left:-10px}
.deliverables li{font-weight:300;font-size:14.5px;color:var(--blue);line-height:24px;padding-left:11px;position:relative}
.deliverables li::before{content:"";position:absolute;left:0;top:8px;width:4px;height:4px;border-radius:50%;background:var(--blue)}

.feature{position:absolute;top:271px;width:290px}
.feature .frame{width:268px;height:130px;background:#fff;border:1px solid #d8d8d8;padding:5px;box-shadow:0 1px 3px rgba(0,0,0,.1)}
.feature .photo{width:256px;height:118px}
.feature h3{margin:10px 0 0 6px;font-weight:400;font-size:14px;color:var(--blue)}
.feature p{margin:6px 0 0 6px;font-family:"Arimo",sans-serif;font-size:12.8px;line-height:15.5px;color:#6e6e6e;letter-spacing:.3px;white-space:nowrap}
.feature-general{left:111px}
.feature-claims{left:415px}
.feature-claims h3,.feature-claims p{margin-left:2px}
.photo-team{background:linear-gradient(135deg,#d9dde2 0%,#9a8b7c 35%,#e8e6e2 60%,#5a6470 100%)}
.photo-office{background:linear-gradient(135deg,#f0f0ee 0%,#2f3236 35%,#b58668 55%,#e3e5e8 100%)}

.news{position:absolute;left:796px;top:262px;width:295px;height:230px}
.news h2{font-weight:300;font-size:19px;color:#555}
.news-item{position:absolute;left:0;width:295px;height:70px}
.news-first{top:50px}
.news-second{top:140px}
.news-rule{position:absolute;left:0;top:124px;width:295px;border-top:1px dotted #cfcfcf}
.date{position:absolute;left:2px;top:2px;width:40px}
.date .day{width:38px;height:36px;background:#fff;border:1px solid #dcdcdc;border-radius:3px;box-shadow:0 2px 2px rgba(0,0,0,.12);text-align:center;font-weight:700;font-size:20px;color:#4a4a4a;line-height:34px}
.date .month{text-align:center;font-family:"Arimo",sans-serif;font-size:9.5px;color:#999;margin-top:6px}
.news-body{position:absolute;left:57px;top:0;font-family:"Arimo",sans-serif}
.news-body .title{font-size:13.5px;color:#444}
.news-body .place{font-size:11.5px;color:#777;margin-top:4px}
.news-body .time{font-size:11.5px;color:#555;margin-top:6px}

/* footer */
.site-footer{position:absolute;left:0;top:1122px;width:1200px;height:68px;background:var(--footer)}
.copyright{position:absolute;left:116px;top:18px;font-family:"Arimo",sans-serif;font-size:12.5px;color:var(--footer-text)}
.legal{position:absolute;left:124px;top:37px;font-family:"Arimo",sans-serif;font-size:12.5px;color:var(--footer-text)}
.legal a{color:var(--footer-link);text-decoration:none}
.footer-icons{position:absolute;left:900px;top:17px;display:flex;gap:10px;align-items:center}
</style>
</head>
<body>
<div class="page">

<header class="site-header">
  <div class="brand">
    <span class="brand-square"></span>
    <span class="brand-name">Vantrel 4 Management Limited</span>
  </div>
  <div class="social-buttons">
    <span class="btn-like">Like</span>
    <span class="btn-count">27m</span>
    <span class="btn-follow">Follow</span>
  </div>
  <nav class="main-nav">
    <a href="#">Home</a>
    <a href="#">Why work with us?</a>
    <a href="#">Services</a>
    <a href="#">Our sales Process</a>
    <a href="#">FAQs</a>
    <a href="#">Proven Success</a>
    <a href="#">News</a>
  </nav>
</header>

<section class="hero">
  <div class="hero-photo" role="img" aria-label="Large yellow bucket-wheel excavator under a cloudy blue sky"></div>
  <h1 class="hero-title">Managemnent Limited</h1>
  <p class="hero-copy">Effective Contract Management is essential for a project to be successful.&nbsp; The contract represents the agreed rights and obliga-tions made by each party to one another.&nbsp; In addition there may be many underlying obligations some stated explicitly in the contract while others may be implied. These obligations form the baseline frame of reference.&nbsp; Vantrel 4 Management Limited will assist the project team to identify the contract baseline deliverables.&nbsp; Once</p>
  <div class="cta">
    <div class="cta-signup">
      <svg width="36" height="24" viewBox="0 0 36 24"><rect x="1" y="1" width="34" height="22" fill="#111"/><path d="M1 1 L18 14 L35 1 M1 23 L13 11 M35 23 L23 11" stroke="#fff" stroke-width="2" fill="none"/></svg>
      <span class="big">SIGN UP</span>
      <span class="small">To our mailing list</span>
    </div>
    <div class="cta-contact">
      <div class="label">Contact Us Today</div>
      <div class="phone">(021) 555-0148</div>
    </div>
    <div class="cta-or">or</div>
  </div>
</section>

<main class="content">
  <section class="prime">
    <h2 class="section-title">Prime Contract Administration</h2>
    <p>Depending on the contracting arrangement adopted by the contractor certain scope may be sub con-tracted to a third party (sub contractor / supplier) due to the specialist nature of the work.&nbsp; In many instances the amount of work sub contracted may in fact exceed the work to be performed directly by the principal contractor.&nbsp; While the work may be sub contracted on a lump sum basis, it remains vital to the project team to manage these sub contractors to ensure a successful outcome for the project.&nbsp; Sub contract management (administration) is often a complex and time consuming task especially if the systems and processes needed are not sufficiently mature.&nbsp; Our approach is to equip the project team with these systems and processes, procedures and tools to enable them to quickly implement the control required without expending a significant time developing a sub contract administration system.</p>
  </section>

  <div class="divider"></div>

  <section class="deliverables">
    <h2 class="section-title">Sub Contractor Deliverables</h2>
    <ul>
      <li>Contract Baseline Schedule</li>
      <li>Monthly Reporting Requirements</li>
      <li>Site Instructions</li>
      <li>Requests for Information (RFI)</li>
      <li>Change Requests</li>
      <li>Mobilisation Plan</li>
      <li>Resource Plans</li>
    </ul>
  </section>

  <article class="feature feature-general">
    <div class="frame"><div class="photo photo-team" role="img" aria-label="Team of colleagues reviewing work together at a desk"></div></div>
    <h3>General</h3>
    <p>Contract Appraisal Meeting &nbsp;&nbsp; Responsibil-<br>ity Assignment Matrix Customer Supplied<br>Deliverables</p>
  </article>

  <article class="feature feature-claims">
    <div class="frame"><div class="photo photo-office" role="img" aria-label="Business professionals in an office meeting"></div></div>
    <h3>Claims &amp; Dispute</h3>
    <p>Schedule Claims Analysis Schedule Impact<br>Management Notices and Claim Preparation</p>
  </article>

  <section class="news">
    <h2>Upcoming News</h2>
    <div class="news-item news-first">
      <div class="date"><div class="day">16</div><div class="month">SEP</div></div>
      <div class="news-body">
        <div class="title">Sunday Services</div>
        <div class="place">Harbour City, Elm St.</div>
        <div class="time">08:45 AM</div>
      </div>
    </div>
    <div class="news-rule"></div>
    <div class="news-item news-second">
      <div class="date"><div class="day">21</div><div class="month">SEP</div></div>
      <div class="news-body">
        <div class="title">General Young Women Meeting</div>
        <div class="place">Westbrook, Cedar Way</div>
        <div class="time">12:30</div>
      </div>
    </div>
  </section>
</main>

<footer class="site-footer">
  <div class="copyright">©2012 Vantrel4 Management Limited. All Rights Reserved .Inc</div>
  <div class="legal"><a href="#">Terms of Use</a> | <a href="#">Privacy Policy</a></div>
  <div class="footer-icons">
    <svg width="18" height="28" viewBox="0 0 18 28"><circle cx="9" cy="14" r="8" fill="#fff"/></svg>
    <svg width="34" height="28" viewBox="0 0 34 28"><circle cx="17" cy="14" r="11" fill="#fff"/></svg>
    <svg width="34" height="28" viewBox="0 0 34 28"><rect x="1" y="3" width="32" height="22" fill="#fff"/><path d="M1 3 L17 16 L33 3 M1 25 L13 13 M33 25 L21 13" stroke="#050505" stroke-width="2" fill="none"/></svg>
    <svg width="28" height="28" viewBox="0 0 28 28"><rect x="7" y="1" width="14" height="8" fill="#fff"/><rect x="1" y="9" width="26" height="12" rx="2" fill="#fff"/><rect x="7" y="17" width="14" height="10" fill="#fff" stroke="#050505" stroke-width="2"/></svg>
    <svg width="26" height="28" viewBox="0 0 26 28"><rect x="10" y="2" width="6" height="24" fill="#fff"/><rect x="1" y="11" width="24" height="6" fill="#fff"/></svg>
  </div>
</footer>

</div>
</body>
</html>
```